bright meridian advisory needs a business card

i need a business card with a logo that will also be used on the website. The company name is "Bright Meridian Advisory"
The business is an advisory and training organisation that specialises in finding a companys 'natural sequence' to success but we will also provide mentoring and counselling to individuals that want to unlock their potential. The process is unique and not full of the normal corporate bullshit so the card should be 'different' and innovative in use of texture, colour, layout etc...I have no guiding principles for you but if you were the head of a new company lloking to make a great first impression what would your card look like? It should have enough of the corporate that the stiffs dont get scared but should be cool enough that the cool kids get it :-)

Target Market(s)

Companies and people looking to grow their staff capabilities. Specialising in IT but can transcend that to other lines of business.

Industry/Entity Type

It Company

Contact Information for Business Card

usuall placeholder stuff Name, Number etc

Requirements
Must have
• cool and innovative logo and use of space
Nice to have
• Background image, subtle use of the caffeine molecule
• A rollable business card similar to the attached image. Would be nice if either side of the card could be half of a DNA helix and by rolling 2 sides together they could connect at one or more points....Perhaps the strands between have a message?
Should not have
• boring usual business card look and feel

```html
<!DOCTYPE html>
<html lang="en">
<head>
<meta charset="utf-8">
<title>Bright Meridian Advisory – Business Card</title>
<link href="https://fonts.googleapis.com/css2?family=Roboto:wght@300;400&display=swap" rel="stylesheet">
<style>
  :root {
    --page: #eceff1;
    --blue: #0aa6d8;
    --blue-deep: #0a8fc8;
    --blue-light: #19c0e8;
    --grey-strip: #6d6e70;
    --white: #ffffff;
    --ink: #4a4a4a;
    --ink-soft: #5c5c5c;
  }
  * { box-sizing: border-box; margin: 0; padding: 0; }
  html, body { width: 1200px; height: 1023px; overflow: hidden; }
  body {
    background: var(--page);
    font-family: "Roboto", Arial, sans-serif;
    position: relative;
  }
  .card {
    position: absolute;
    left: 200px;
    width: 800px;
    height: 457px;
    border-radius: 22px;
    overflow: hidden;
    box-shadow: 0 6px 18px rgba(0,0,0,0.18);
  }
  .card-front { top: 36px; background: var(--white); }
  .card-back {
    top: 533px;
    background: radial-gradient(ellipse at 65% 35%, var(--blue-light) 0%, var(--blue) 55%, var(--blue-deep) 100%);
  }
  .front-shapes { position: absolute; inset: 0; width: 800px; height: 457px; }

  .brand {
    position: absolute;
    display: flex;
    align-items: center;
    gap: 16px;
  }
  .brand-front { left: 44px; top: 46px; }
  .brand-mark { border-radius: 50%; flex: none; }
  .brand-front .brand-mark { width: 50px; height: 50px; background: var(--blue); }
  .brand-name { font-weight: 400; letter-spacing: 0.3px; white-space: nowrap; }
  .brand-front .brand-name { color: var(--blue); font-size: 30px; }

  .person { position: absolute; left: 150px; top: 170px; }
  .person-name { font-size: 40px; font-weight: 400; color: var(--ink); letter-spacing: 0.5px; }
  .person-title { font-size: 19px; color: var(--blue); margin-top: 2px; }

  .contact {
    position: absolute;
    left: 150px;
    top: 262px;
    list-style: none;
  }
  .contact li {
    display: flex;
    align-items: center;
    gap: 12px;
    font-size: 16px;
    font-weight: 300;
    color: var(--ink-soft);
    height: 28px;
    letter-spacing: 0.4px;
  }
  .contact svg { width: 17px; height: 17px; flex: none; }

  .brand-back {
    left: 0; right: 0; top: 0; bottom: 0;
    flex-direction: column;
    justify-content: center;
    gap: 26px;
  }
  .brand-back .brand-mark {
    width: 96px; height: 96px;
    border: 8px solid var(--white);
  }
  .brand-back .brand-name { color: var(--white); font-size: 46px; }
</style>
</head>
<body>

<section class="card card-front" aria-label="Card front">
  <svg class="front-shapes" viewBox="0 0 800 457" aria-hidden="true">
    <defs>
      <linearGradient id="sideBlue" x1="0" y1="0" x2="1" y2="1">
        <stop offset="0" stop-color="#1cc2ea"/>
        <stop offset="1" stop-color="#0a92cb"/>
      </linearGradient>
    </defs>
    <rect width="800" height="457" fill="url(#sideBlue)"/>
    <polygon points="470,0 600,0 690,330 650,402" fill="var(--grey-strip)"/>
    <polygon points="470,0 545,0 665,402 612,402" fill="var(--blue-light)"/>
    <polygon points="0,0 470,0 612,402 0,402" fill="var(--white)"/>
    <rect x="0" y="402" width="800" height="55" fill="var(--blue)"/>
  </svg>

  <div class="brand brand-front">
    <span class="brand-mark"></span>
    <span class="brand-name">Bright Meridian Advisory</span>
  </div>

  <div class="person">
    <p class="person-name">Your Name</p>
    <p class="person-title">Title</p>
  </div>

  <ul class="contact">
    <li>
      <svg viewBox="0 0 24 24"><path fill="var(--blue)" d="M6.6 10.8a15.1 15.1 0 0 0 6.6 6.6l2.2-2.2a1 1 0 0 1 1-.25 11.4 11.4 0 0 0 3.6.6 1 1 0 0 1 1 1V20a1 1 0 0 1-1 1A17 17 0 0 1 3 4a1 1 0 0 1 1-1h3.5a1 1 0 0 1 1 1c0 1.25.2 2.45.6 3.6a1 1 0 0 1-.25 1z"/></svg>
      44-210-77830
    </li>
    <li>
      <svg viewBox="0 0 24 24"><rect x="3" y="5" width="18" height="14" fill="none" stroke="var(--blue)" stroke-width="1.8"/><path d="M3 5l9 8 9-8" fill="none" stroke="var(--blue)" stroke-width="1.8"/></svg>
      hello@brightmeridian.net
    </li>
    <li>
      <svg viewBox="0 0 24 24"><circle cx="12" cy="12" r="9" fill="none" stroke="var(--blue)" stroke-width="1.8"/><path d="M3 12h18M12 3c3 3 3 15 0 18M12 3c-3 3-3 15 0 18" fill="none" stroke="var(--blue)" stroke-width="1.5"/></svg>
      www.brightmeridian.co.uk
    </li>
    <li>
      <svg viewBox="0 0 24 24"><path fill="var(--blue)" d="M12 2a7 7 0 0 0-7 7c0 5 7 13 7 13s7-8 7-13a7 7 0 0 0-7-7zm0 9.5A2.5 2.5 0 1 1 12 6.5a2.5 2.5 0 0 1 0 5z"/></svg>
      Your address
    </li>
  </ul>
</section>

<section class="card card-back" aria-label="Card back">
  <div class="brand brand-back">
    <span class="brand-mark"></span>
    <span class="brand-name">Bright Meridian Advisory</span>
  </div>
</section>

</body>
</html>
```